Make the design for the landing page of BrightKettle.com

Veltrix is framework (software to build websites)
Goal:
Build a professional landing page to offer free Veltrix consultancy sessions in exchange for an email address and to promote your paid services.
🎯 Primary Objective
Convert visitors into leads by offering a free Veltrix code audit or strategy session. Capture their email and optionally allow them to directly book a call or hire your services.
🧠 Target Audience
>Companies and startups with Veltrix apps
>CTOs and tech leads managing legacy Veltrix code
>Freelance developers looking to improve their architecture
>Product owners facing bugs or scaling issues
📐 Suggested Page Structure
1. Hero Section (Top of Page - Above the Fold)
Headline (focused on pain/problem):
“Is your Veltrix app slow, outdated or full of bugs?”
Subheadline (clear promise of value):
“Book a free Veltrix code audit and get actionable insights in just 30 minutes.”
Primary CTA (email capture form):
Email input
Button: “Schedule Free Consultation”
Secondary CTA Button:
“Free Consultancy” or “Hire My Services”
✅ Make this CTA bold, highly visible, and frictionless
✅ You can use Calendly, TidyCal, or a simple form for scheduling
2. Section: “Are you struggling with any of these?”
Use a vertical scroll experience with checkmarks or icons to highlight common pain points:
🔼 Upgrading PHP / Veltrix
🧪 No automated tests
🐛 Recurring bugs
🔐 Security issues
🐢 Slow performance
🧱 Messy architecture or no clear structure
📦 Outdated packages / dependencies
Make this visually engaging — for example, animated list items as the user scrolls down.
3. What You Get With a Free Audit
A personalized code review or system analysis
Architecture & performance insights
No commitment, no spam
+12 years of Veltrix experience
Delivered via a video call or written feedback
4. About Me / Why Trust Me
Short section introducing you:
Your experience with Veltrix (12+ years)
Notable companies, projects, or logos (if any)
Repolyn / Medium / Open Source contributions
Maybe include a friendly photo or avatar
5. Call to Action (Repeat CTA)
Reinforce the offer:
“Let’s fix your Veltrix headaches together — for free.”
Button: “Book My Free Call”
Optional email input form again (for easy access)
6. Testimonials (Optional but Recommended)
If you already have satisfied clients:
2-3 short quotes with names and roles
Example: “Tobías helped us restructure our legacy Veltrix codebase in a week. Highly recommended!”
7. FAQ Section (Optional)
Common questions to eliminate hesitation:
What happens after I submit my email?
Is the consultancy really free?
What kind of projects do you work with?
How long does the call last?
8. Footer
Quick access buttons:
“Schedule Consultation”
“Hire My Services”
Contact email
Linked social profiles or Repolyn
✨ Design Style & Inspirations
Clean, minimalist layout (like plumfernworks.io, but with more obvious CTAs)
Technical yet friendly tone
Use soft animations and icons to break sections
What I would like to see?
An obvious CTA in the middle to the page in order to schedule a 30-mins free consultancy .
also a when you scroll you will see something like
"These problems are common for you"
With the list of common PHP/Veltrix problems.
Also would like a button in the top right that says
"Audit me now" like "Get unstuck" in https://plumfernworks.io/
Take inspiration from:
https://plumfernworks.io/
https://www.zelvanhub.io/
Use this as the logo
https://quorbixfield48.pagelet.site/png/logo
Consultancy Project
1 page

```html
<!DOCTYPE html>
<html lang="en">
<head>
<meta charset="utf-8">
<title>BrightKettle.com – Free Veltrix Code Audit</title>
<link href="https://fonts.googleapis.com/css2?family=Poppins:wght@400;500;600;700&display=swap" rel="stylesheet">
<style>
:root{
  --red:#f32b1f;
  --red-dark:#c8170f;
  --ink:#111111;
  --text:#2b2b2b;
  --muted:#666666;
  --grey:#f1f1f1;
  --line:#e2e2e2;
  --white:#ffffff;
}
*{box-sizing:border-box;margin:0;padding:0}
html,body{width:1200px;height:4785px;overflow:hidden}
body{position:relative;font-family:'Poppins',sans-serif;color:var(--text);background:var(--white)}
.abs{position:absolute}
section,header,footer{position:absolute;left:0;width:1200px}
.red{color:var(--red)}
.rule{height:3px;background:var(--red);position:absolute}

/* header */
.site-header{top:0;height:120px;background:var(--white)}
.brand{left:72px;top:40px;height:40px;padding:0 18px 0 14px;border-radius:20px;background:#fde3e1;display:flex;align-items:center;gap:10px;font-weight:600;font-size:18px;color:var(--red)}
.brand-dot{width:14px;height:14px;border-radius:50%;background:var(--red)}
.nav{left:466px;top:48px;display:flex;gap:38px;font-size:14px;font-weight:500;color:var(--ink)}
.nav .active{color:var(--red)}
.btn{display:inline-flex;align-items:center;justify-content:center;border-radius:30px;font-weight:500;white-space:nowrap}
.btn-red{background:var(--red);color:var(--white)}
.btn-outline{border:1.5px solid var(--red);color:var(--red);background:var(--white)}
.btn-white{background:var(--white);color:var(--red)}
.btn-ghost{border:1.5px solid var(--white);color:var(--white)}
.audit-btn{left:983px;top:42px;width:150px;height:36px;font-size:14px}

/* hero */
.hero{top:120px;height:593px;background:linear-gradient(100deg,#5a4a48 0%,#7b6a66 45%,#9a8c88 70%,#b7aca8 100%)}
.hero-bg{position:absolute;inset:0}
.hero h1{left:65px;top:150px;width:640px;font-size:52px;line-height:64px;font-weight:600;color:var(--ink);text-transform:uppercase;letter-spacing:-0.5px;white-space:nowrap}
.hero p{left:67px;top:368px;font-size:15px;color:var(--ink);white-space:nowrap}
.form-card{left:720px;top:103px;width:417px;height:387px;background:var(--white);border-radius:8px}
.field{position:absolute;height:32px;border:1.5px solid #dcdcdc;border-radius:3px;font-size:8px;color:#9a9a9a;padding:10px 10px;background:var(--white)}
.form-actions{position:absolute;display:flex;gap:8px}
.form-actions .btn{height:30px;font-size:10px;font-weight:600}

/* struggles */
.struggles{top:713px;height:454px;background:var(--white)}
.pain{position:absolute;display:flex;align-items:center;gap:16px;font-size:15px;color:var(--ink)}
.pain svg{width:44px;height:44px;flex:none}
.struggles h2{left:660px;top:160px;width:500px;text-align:center;font-size:40px;line-height:48px;font-weight:600;color:var(--ink)}

/* what you get */
.benefits{top:1167px;height:500px;background:var(--grey)}
.section-title{font-size:40px;line-height:48px;font-weight:600;color:var(--ink);text-transform:uppercase}
.benefits .section-title{left:115px;top:48px}
.photo{position:absolute;border-radius:8px}
.benefit{position:absolute;left:598px;display:flex;gap:18px;font-size:26px;line-height:32px;color:var(--ink);width:460px}
.benefit svg{width:30px;height:30px;flex:none;margin-top:2px}

/* about */
.about{top:1667px;height:540px;background:var(--white)}
.about .section-title{left:104px;top:96px}
.about p{left:104px;top:175px;width:432px;font-size:14px;line-height:24px;text-align:justify;color:var(--ink)}
.about .btn{left:104px;top:391px;width:162px;height:47px;font-size:14px}
.exp-card{left:591px;top:328px;width:269px;height:141px;background:var(--red);border-radius:12px;color:var(--white);text-align:center;padding-top:24px}
.exp-card strong{display:block;font-size:48px;line-height:52px;font-weight:600}
.exp-card span{font-size:18px;font-weight:600}

/* logos */
.partners{top:2207px;height:331px;background:var(--grey)}
.partner{position:absolute;top:130px;width:150px;text-align:center;display:flex;flex-direction:column;align-items:center;gap:6px;font-size:36px;font-weight:600;color:#555}
.partner i{width:52px;height:52px;border-radius:50%;background:#555;display:block}
.arrow{position:absolute;top:148px;width:24px;height:34px}

/* cta */
.cta{top:2538px;height:494px;background:linear-gradient(110deg,#a9c2d6 0%,#d6e3ee 40%,#c2d4e3 70%,#9db6cb 100%)}
.cta-form{left:97px;top:50px;width:418px;height:390px;background:var(--red);border-radius:4px}
.cta-form .field{background:transparent;border-color:var(--white);color:var(--white)}
.cta h2{left:570px;top:120px;font-size:48px;line-height:58px;font-weight:600;color:var(--ink);white-space:nowrap}
.cta .book{left:587px;top:325px;width:182px;height:38px;font-size:14px}

/* testimonials */
.testimonials{top:3032px;height:665px;background:#f6f6f6}
.center-title{left:0;width:1200px;text-align:center}
.quote{position:absolute;top:220px;width:270px;height:282px;background:var(--white);border:1.5px solid var(--line);border-radius:8px;padding:34px 22px}
.quote p{font-size:13px;line-height:23px;text-align:justify;color:var(--ink)}
.quote .who{display:flex;align-items:center;gap:16px;margin-top:16px}
.avatar{width:68px;height:68px;border-radius:50%;background:linear-gradient(135deg,#d9c3a9,#8a6e55);flex:none}
.who b{display:block;font-size:14px;font-weight:600;color:var(--ink)}
.stars{color:#f4b400;font-size:18px;letter-spacing:4px}
.dots{left:567px;top:565px;display:flex;gap:8px}
.dots i{width:12px;height:12px;border-radius:50%;border:1.5px solid var(--red);display:block}
.dots i:first-child{background:var(--red)}

/* faq */
.faq{top:3697px;height:680px;background:var(--white)}
.faq-item{position:absolute;left:106px;width:522px;border:1.5px solid #f6b3ae;border-radius:8px;padding:18px 22px}
.faq-item h3{font-size:15px;font-weight:500;color:var(--red)}
.faq-item p{font-size:13px;line-height:23px;color:var(--ink);margin-top:6px;width:440px}
.toggle{position:absolute;right:22px;top:18px;width:22px;height:22px;border-radius:50%;background:var(--red);color:var(--white);font-size:16px;line-height:21px;text-align:center;font-weight:600}

/* footer */
.site-footer{top:4377px;height:408px;background:var(--red);color:var(--white)}
.col-title{position:absolute;top:95px;font-size:19px;font-weight:500;text-transform:uppercase}
.col-list{position:absolute;top:158px;list-style:none;font-size:14px;line-height:26px}
.col-list li::before{content:"→ ";font-weight:600}
.news-text{left:87px;top:158px;width:300px;font-size:13px;line-height:20px}
.news-input{left:87px;top:214px;width:270px;height:28px;border-radius:14px;background:var(--white);color:#999;font-size:12px;padding:5px 18px}
.news-btn{left:87px;top:256px;width:112px;height:32px;background:var(--red-dark);font-size:14px}
.contact{position:absolute;left:901px;display:flex;gap:16px;font-size:13px;line-height:18px}
.contact i{width:26px;height:26px;border-radius:4px;background:var(--white);display:flex;align-items:center;justify-content:center;flex:none}
.bottom-bar{left:0;top:353px;width:1200px;height:55px;background:var(--red-dark);font-size:12px;padding:20px 67px}
.socials{position:absolute;right:67px;top:16px;display:flex;gap:8px}
.socials i{width:22px;height:22px;background:var(--red);border-radius:3px;display:block}
</style>
</head>
<body>

<header class="site-header">
  <div class="abs brand"><span class="brand-dot"></span>BrightKettle</div>
  <nav class="abs nav"><span class="active">Home</span><span>About Us</span><span>Services</span><span>Testimonials</span><span>Contact Us</span></nav>
  <a class="abs btn btn-red audit-btn">Audit Me Now</a>
</header>

<section class="hero">
  <div class="hero-bg" role="img" aria-label="Developer typing on a laptop with code overlay"></div>
  <h1 class="abs">Is your Veltrix app<br>slow, outdated<br>or full of bugs?</h1>
  <p class="abs">Book a free Veltrix code audit and get actionable insights in just 30 minutes.</p>
  <div class="abs form-card">
    <div class="field" style="left:24px;top:50px;width:176px">First Name</div>
    <div class="field" style="left:217px;top:50px;width:176px">Last Name</div>
    <div class="field" style="left:24px;top:97px;width:176px">Phone</div>
    <div class="field" style="left:217px;top:97px;width:176px">Date</div>
    <div class="field" style="left:24px;top:142px;width:369px">Email</div>
    <div class="field" style="left:24px;top:190px;width:369px;height:84px">Message</div>
    <div class="form-actions" style="left:24px;top:300px">
      <a class="btn btn-red" style="width:180px">Schedule Free Consultation</a>
      <a class="btn btn-outline" style="width:146px">Hire My Services</a>
    </div>
  </div>
</section>

<section class="struggles">
  <div class="pain" style="left:75px;top:86px"><svg viewBox="0 0 44 44"><rect x="6" y="4" width="32" height="36" rx="3" fill="none" stroke="#f32b1f" stroke-width="2.5"/><rect x="2" y="16" width="26" height="12" rx="2" fill="#f32b1f"/></svg>Upgrading PHP / Veltrix</div>
  <div class="pain" style="left:75px;top:164px"><svg viewBox="0 0 44 44"><rect x="8" y="4" width="24" height="32" rx="3" fill="#f32b1f"/><circle cx="32" cy="32" r="9" fill="#f32b1f" stroke="#fff" stroke-width="2"/><path d="M28 32l3 3 5-6" stroke="#fff" stroke-width="2" fill="none"/></svg>No Automated Tests</div>
  <div class="pain" style="left:75px;top:244px"><svg viewBox="0 0 44 44"><rect x="4" y="6" width="36" height="30" rx="3" fill="none" stroke="#f32b1f" stroke-width="2.5"/><circle cx="20" cy="21" r="8" fill="none" stroke="#f32b1f" stroke-width="2.5"/><path d="M26 27l8 8" stroke="#f32b1f" stroke-width="3"/></svg>Recurring Bugs</div>
  <div class="pain" style="left:75px;top:322px"><svg viewBox="0 0 44 44"><rect x="14" y="16" width="24" height="20" rx="3" fill="#f32b1f"/><path d="M19 16v-5a7 7 0 0 1 14 0v5" stroke="#f32b1f" stroke-width="3" fill="none"/><path d="M8 40l8-14 8 14z" fill="#f32b1f"/></svg>Security issues</div>
  <div class="pain" style="left:353px;top:86px"><svg viewBox="0 0 44 44"><path d="M6 28a16 16 0 0 1 32 0z" fill="#f32b1f"/><circle cx="14" cy="34" r="6" fill="none" stroke="#f32b1f" stroke-width="2.5"/></svg>Slow performance</div>
  <div class="pain" style="left:353px;top:164px"><svg viewBox="0 0 44 44"><path d="M22 6l16 8-16 8-16-8z M6 22l16 8 16-8 M6 30l16 8 16-8" fill="none" stroke="#f32b1f" stroke-width="2.5"/></svg>Messy architecture</div>
  <div class="pain" style="left:353px;top:244px"><svg viewBox="0 0 44 44"><path d="M22 4l18 9v18l-18 9-18-9V13z" fill="#f32b1f"/><path d="M4 13l18 9 18-9M22 22v18" stroke="#fff" stroke-width="2" fill="none"/></svg>Outdated packages /<br>dependencies</div>
  <h2 class="abs"><span class="red">ARE YOU STRUGGLING</span><br>WITH ANY OF THESE?</h2>
  <div class="rule" style="left:827px;top:268px;width:150px"></div>
</section>

<section class="benefits">
  <h2 class="abs section-title"><span class="red">What you get</span><br>with a free audit</h2>
  <div class="rule" style="left:115px;top:149px;width:152px"></div>
  <div class="photo" role="img" aria-label="Code on a monitor" style="left:193px;top:189px;width:138px;height:120px;background:linear-gradient(135deg,#1d2a2a,#3b4a3e)"></div>
  <div class="photo" role="img" aria-label="Laptop with code editor" style="left:312px;top:189px;width:138px;height:120px;background:linear-gradient(135deg,#2b2218,#6a5032)"></div>
  <div class="photo" role="img" aria-label="Laptop on a desk" style="left:193px;top:320px;width:110px;height:122px;background:linear-gradient(135deg,#2b3326,#8a5b34)"></div>
  <div class="photo" role="img" aria-label="Hands typing on a laptop" style="left:312px;top:320px;width:138px;height:122px;background:linear-gradient(135deg,#3e5a76,#a9b9c8)"></div>
  <div class="benefit" style="top:54px"><svg viewBox="0 0 30 30"><circle cx="15" cy="15" r="12" fill="none" stroke="#f32b1f" stroke-width="2.5"/><path d="M9 15l5 5 11-12" stroke="#f32b1f" stroke-width="3" fill="none"/></svg><span>A personalized code review or system analysis</span></div>
  <div class="benefit" style="top:151px"><svg viewBox="0 0 30 30"><circle cx="15" cy="15" r="12" fill="none" stroke="#f32b1f" stroke-width="2.5"/><path d="M9 15l5 5 11-12" stroke="#f32b1f" stroke-width="3" fill="none"/></svg><span>Architecture &amp; performance<br>insights</span></div>
  <div class="benefit" style="top:249px"><svg viewBox="0 0 30 30"><circle cx="15" cy="15" r="12" fill="none" stroke="#f32b1f" stroke-width="2.5"/><path d="M9 15l5 5 11-12" stroke="#f32b1f" stroke-width="3" fill="none"/></svg><span>No commitment, no spam</span></div>
  <div class="benefit" style="top:314px"><svg viewBox="0 0 30 30"><circle cx="15" cy="15" r="12" fill="none" stroke="#f32b1f" stroke-width="2.5"/><path d="M9 15l5 5 11-12" stroke="#f32b1f" stroke-width="3" fill="none"/></svg><span>+12 years of Veltrix experience</span></div>
  <div class="benefit" style="top:380px"><svg viewBox="0 0 30 30"><circle cx="15" cy="15" r="12" fill="none" stroke="#f32b1f" stroke-width="2.5"/><path d="M9 15l5 5 11-12" stroke="#f32b1f" stroke-width="3" fill="none"/></svg><span>Delivered via a video call or written feedback</span></div>
</section>

<section class="about">
  <h2 class="abs section-title"><span class="red">About</span> Us</h2>
  <div class="rule" style="left:104px;top:143px;width:150px"></div>
  <p class="abs">Lorem ipsum dolor sit amet, consectetur adipiscing elit, sed do eiusmod tempor incididunt ut labore et dolore magna aliqua. Ut enim ad minim veniam, quis nostrud exercitation ullamco laboris nisi ut aliquip ex ea commodo consequat. Duis aute irure dolor in reprehenderit in voluptate velit esse cillum dolore eu fugiat nulla pariatur. Excepteur sint occaecat cupidatat non proident, sunt in culpa qui officia deserunt mollit anim id est laborum.</p>
  <a class="abs btn btn-red">Know More</a>
  <div class="photo" role="img" aria-label="Code editor on a dark screen" style="left:591px;top:72px;width:269px;height:245px;border-radius:12px;background:linear-gradient(160deg,#0f1c24,#24343e 60%,#101a20)"></div>
  <div class="abs exp-card"><strong>12+</strong><span>YEARS OF EXPERIENCE</span></div>
  <div class="photo" role="img" aria-label="Developer working on a laptop at an office desk" style="left:871px;top:72px;width:227px;height:397px;border-radius:12px;background:linear-gradient(170deg,#7d7a74,#bfb8ae 45%,#c8453a 70%,#5a514a)"></div>
</section>

<section class="partners">
  <svg class="arrow" style="left:109px" viewBox="0 0 24 34"><path d="M18 4L6 17l12 13" stroke="#f32b1f" stroke-width="4" fill="none"/></svg>
  <div class="partner" style="left:200px"><i></i>Repolyn</div>
  <div class="partner" style="left:417px"><i></i>Repolyn</div>
  <div class="partner" style="left:633px"><i></i>Repolyn</div>
  <div class="partner" style="left:850px"><i></i>Repolyn</div>
  <svg class="arrow" style="left:1056px" viewBox="0 0 24 34"><path d="M6 4l12 13L6 30" stroke="#f32b1f" stroke-width="4" fill="none"/></svg>
</section>

<section class="cta">
  <div class="abs" role="img" aria-label="Blurred code on a blue screen" style="inset:0"></div>
  <div class="abs cta-form">
    <div class="field" style="left:24px;top:50px;width:176px">First Name</div>
    <div class="field" style="left:218px;top:50px;width:176px">Last Name</div>
    <div class="field" style="left:24px;top:98px;width:176px">Phone</div>
    <div class="field" style="left:218px;top:98px;width:176px">Date</div>
    <div class="field" style="left:24px;top:143px;width:370px;height:30px">Email</div>
    <div class="field" style="left:24px;top:190px;width:370px;height:84px">Message</div>
    <div class="form-actions" style="left:24px;top:288px">
      <a class="btn btn-white" style="width:180px">Schedule Free Consultation</a>
      <a class="btn btn-ghost" style="width:146px">Hire My Services</a>
    </div>
  </div>
  <h2 class="abs">LET’S FIX YOUR<br>VELTRIX HEADACHES<br>TOGETHER – FOR FREE.</h2>
  <a class="abs btn btn-red book">BOOK MY FREE CALL</a>
</section>

<section class="testimonials">
  <h2 class="abs section-title center-title" style="top:110px"><span class="red">Our</span> Testimonials</h2>
  <div class="rule" style="left:525px;top:176px;width:150px"></div>
  <div class="quote" style="left:145px"><p>"Lorem ipsum dolor sit amet, consectetur adipiscing elit, sed do eiusmod tempor incididunt ut labore et dolore magna aliqua. Quis ipsum suspendisse ultrices gravida."</p><div class="who"><div class="avatar" role="img" aria-label="Client portrait"></div><div><b>DICKENS DEN</b><span class="stars">★★★★★</span></div></div></div>
  <div class="quote" style="left:470px"><p>"Lorem ipsum dolor sit amet, consectetur adipiscing elit, sed do eiusmod tempor incididunt ut labore et dolore magna aliqua. Quis ipsum suspendisse ultrices gravida."</p><div class="who"><div class="avatar" role="img" aria-label="Client portrait"></div><div><b>WILLIAMS</b><span class="stars">★★★★★</span></div></div></div>
  <div class="quote" style="left:793px"><p>"Lorem ipsum dolor sit amet, consectetur adipiscing elit, sed do eiusmod tempor incididunt ut labore et dolore magna aliqua. Quis ipsum suspendisse ultrices gravida."</p><div class="who"><div class="avatar" role="img" aria-label="Client portrait"></div><div><b>JONATHAN SMITH</b><span class="stars">★★★★★</span></div></div></div>
  <div class="abs dots"><i></i><i></i><i></i><i></i></div>
</section>

<section class="faq">
  <h2 class="abs section-title center-title" style="top:78px"><span class="red">Frequently asked</span><br>questions</h2>
  <div class="rule" style="left:520px;top:178px;width:150px"></div>
  <div class="faq-item" style="top:227px;height:141px"><h3>What happens after I submit my email?</h3><span class="toggle">−</span><p>Lorem ipsum dolor sit amet, consectetur adipiscing elit, sed do eiusmod tempor incididunt ut labore et dolore magna aliqua. Quis ipsum suspendisse ultrices gravida. Risus commodo viverra maecenas accumsan lacus vel facilisis.</p></div>
  <div class="faq-item" style="top:394px;height:63px"><h3>Is the consultancy really free?</h3><span class="toggle">+</span></div>
  <div class="faq-item" style="top:476px;height:63px"><h3>What kind of projects do you work with?</h3><span class="toggle">+</span></div>
  <div class="faq-item" style="top:558px;height:63px"><h3>How long does the call last?</h3><span class="toggle">+</span></div>
  <div class="photo" role="img" aria-label="Code on a screen" style="left:693px;top:229px;width:214px;height:188px;background:linear-gradient(135deg,#c9ced6,#9aa4b2)"></div>
  <div class="photo" role="img" aria-label="Developer with glasses at work" style="left:920px;top:229px;width:171px;height:188px;background:linear-gradient(135deg,#e6e6e6,#7a6a5c)"></div>
  <div class="photo" role="img" aria-label="Code on a screen" style="left:693px;top:432px;width:171px;height:189px;background:linear-gradient(135deg,#b8bfca,#d6dbe2)"></div>
  <div class="photo" role="img" aria-label="Hands typing on a laptop" style="left:877px;top:432px;width:214px;height:189px;background:linear-gradient(135deg,#eeeeee,#8f9aa6)"></div>
</section>

<footer class="site-footer">
  <div class="col-title" style="left:87px">News Letter Sign Up</div>
  <div class="col-title" style="left:448px">Quick Links</div>
  <div class="col-title" style="left:658px">Our Services</div>
  <div class="col-title" style="left:901px">Contact Us</div>
  <p class="abs news-text">To stay up to date on all the latest news and offers from us</p>
  <div class="abs news-input">Enter Mail Id</div>
  <a class="abs btn news-btn" style="color:#fff">Submit</a>
  <ul class="col-list" style="left:448px"><li>Home</li><li>About Us</li><li>Services</li><li>Testimonials</li><li>Contact Us</li></ul>
  <ul class="col-list" style="left:658px"><li>Lorem ipsum</li><li>Lorem ipsum</li><li>Lorem ipsum</li><li>Lorem ipsum</li><li>Lorem ipsum</li></ul>
  <div class="contact" style="top:158px"><i><svg width="14" height="14" viewBox="0 0 14 14"><path d="M3 1l3 3-2 2a8 8 0 0 0 4 4l2-2 3 3-2 2C5 13 1 9 1 3z" fill="#f32b1f"/></svg></i><div>CALL US<br>888 888 8888</div></div>
  <div class="contact" style="top:208px"><i><svg width="14" height="12" viewBox="0 0 14 12"><rect x="0" y="0" width="14" height="12" rx="1" fill="#f32b1f"/><path d="M1 1l6 5 6-5" stroke="#fff" fill="none"/></svg></i><div>EMAIL US<br>info@brightkettle.com</div></div>
  <div class="contact" style="top:264px"><i><svg width="12" height="16" viewBox="0 0 12 16"><path d="M6 0a6 6 0 0 1 6 6c0 4-6 10-6 10S0 10 0 6a6 6 0 0 1 6-6z" fill="#f32b1f"/><circle cx="6" cy="6" r="2" fill="#fff"/></svg></i><div>8865 Lorem ipsum,Lorem<br>ipsum,Lorem ipsum.</div></div>
  <div class="abs bottom-bar">Copyright © 2025 All Rights Reserved By Company name
    <div class="socials"><i></i><i></i><i></i><i></i></div>
  </div>
</footer>

</body>
</html>
```